Online bill payment portal website design

Online Invoice Payment Website

The customer will click on the logos of the institution they want to pay and the payment will be made at the latest stage to write the customer number.

Invoice payment can be made online. Telephone, Television, Internet, Electricity, Water, Natural Gas, and all institutional payments.

Example website : https://www.selvopay.com/

Industry/Entity Type

Invoice

Logo Text

KolayBorcKapat.Net

Number of Pages Required

4 page

Font styles to use
Serif
Sans Serif

Colors
abd036
33a6d7
876aae
e667a6
ec1f27
f37122
85abd2
0555a3
00a990

Requirements
Must have
• Logos of payment institutions
• Credit Card Payment form
• Customer information form
• COntact page
• List of Institutions
• Accept privacy policies in all forms
Nice to have
• Good and new design :)
Should not have
• Same with selvopay.com ! i want new site

```html
<!DOCTYPE html>
<html lang="en">
<head>
<meta charset="utf-8">
<title>Online Pay Now</title>
<link href="https://fonts.googleapis.com/css2?family=Montserrat:wght@400;500;600;700&family=Bitter:wght@300;400&display=swap" rel="stylesheet">
<style>
:root{
  --brand-blue:#0555a3;
  --sky:#33a6d7;
  --lime:#abd036;
  --orange:#f37122;
  --ink:#333a40;
  --muted:#555c63;
  --line:#e6e8eb;
  --footer-bg:#f4f4f4;
  --brown:#5a4636;
  --white:#ffffff;
}
*{box-sizing:border-box;margin:0;padding:0}
html,body{width:1200px;height:1048px;overflow:hidden;background:var(--white)}
body{font-family:'Montserrat',sans-serif;color:var(--ink);position:relative}
.site-header{position:absolute;left:0;top:0;width:1200px;height:89px}
.brand{position:absolute;left:74px;top:31px;font-size:21px;font-weight:700;color:var(--brand-blue);letter-spacing:-.2px}
.brand span{color:var(--sky)}
.main-nav{position:absolute;left:344px;top:37px;display:flex;gap:21px;font-size:13.5px;font-weight:500;color:var(--muted)}
.btn{position:absolute;top:28px;height:33px;font-size:13.5px;font-weight:500;display:flex;align-items:center;justify-content:center;border-radius:2px}
.btn-signup{left:936px;width:90px;border:1px solid var(--sky);color:var(--sky)}
.btn-signin{left:1036px;width:91px;background:var(--orange);color:var(--white)}
.pay-band{position:absolute;left:0;top:89px;width:1200px;height:347px;background:var(--brand-blue)}
.band-title{position:absolute;top:31px;width:100%;text-align:center;font-family:'Bitter',serif;font-weight:300;font-size:22px;color:var(--white)}
.category{position:absolute;top:94px;width:133px;height:133px;border:1px solid rgba(255,255,255,.18);border-radius:2px;color:var(--white);text-align:center}
.category.active{background:var(--sky);border-color:var(--sky)}
.category svg{position:absolute;left:51px;top:33px;width:32px;height:32px;fill:none;stroke:var(--white);stroke-width:1.4;stroke-linecap:round;stroke-linejoin:round}
.category .label{position:absolute;top:88px;width:100%;font-size:14.5px;font-weight:500}
.search{position:absolute;left:390px;top:264px;width:421px;height:46px;background:var(--white);border-radius:2px;display:flex;align-items:center}
.search-tag{position:absolute;left:0;top:0;width:44px;height:46px}
.search-text{position:absolute;left:58px;font-size:14px;color:#9aa0a6}
.section-title{position:absolute;top:484px;width:1200px;text-align:center;font-family:'Bitter',serif;font-weight:300;font-size:22px;color:#222}
.institutions{position:absolute;left:74px;top:561px;width:1052px;height:323px}
.inst{position:absolute;display:flex;align-items:center;justify-content:center;gap:10px}
.inst .mark{width:22px;height:22px;border-radius:50%}
.inst .name{font-size:24px;font-weight:700}
.inst.terra .mark{background:var(--lime)}
.inst.terra .name{color:var(--brown)}
.inst.bright .mark{background:var(--orange)}
.inst.bright .name{color:#222}
.inst.focus{background:var(--white);box-shadow:0 2px 14px rgba(0,0,0,.12);z-index:2}
.vline{position:absolute;width:1px;background:var(--line)}
.hline{position:absolute;height:1px;background:var(--line)}
.site-footer{position:absolute;left:0;top:940px;width:1200px;height:108px;background:var(--footer-bg);font-size:14.5px;color:var(--muted)}
.site-footer .item{position:absolute;top:44px}
.card{position:absolute;top:36px;width:59px;height:37px;border-radius:3px;display:flex;align-items:center;justify-content:center;font-size:11px;font-weight:700}
</style>
</head>
<body>
<header class="site-header">
  <div class="brand">Company <span>Logo</span></div>
  <nav class="main-nav"><span>HOME</span><span>ABOUT</span><span>CONTACT</span></nav>
  <div class="btn btn-signup">SIGN UP</div>
  <div class="btn btn-signin">SIGN IN</div>
</header>

<section class="pay-band">
  <h1 class="band-title">Online Pay Now!</h1>

  <div class="category" style="left:74px">
    <svg viewBox="0 0 32 32"><rect x="11" y="2" width="10" height="28" rx="2"/><line x1="11" y1="7" x2="21" y2="7"/><line x1="11" y1="24" x2="21" y2="24"/><circle cx="16" cy="27" r=".6"/></svg>
    <div class="label">Telephone</div>
  </div>
  <div class="category" style="left:227px">
    <svg viewBox="0 0 32 32"><rect x="2" y="8" width="28" height="20" rx="2"/><rect x="5" y="11" width="22" height="14"/><line x1="11" y1="3" x2="16" y2="8"/><line x1="21" y1="3" x2="16" y2="8"/></svg>
    <div class="label">Television</div>
  </div>
  <div class="category" style="left:380px">
    <svg viewBox="0 0 32 32"><circle cx="16" cy="16" r="14"/><circle cx="16" cy="16" r="10"/><circle cx="16" cy="16" r="6"/><circle cx="16" cy="16" r="2"/></svg>
    <div class="label">Internet</div>
  </div>
  <div class="category active" style="left:534px">
    <svg viewBox="0 0 32 32"><path d="M12 22c0-4-4-6-4-11a8 8 0 0 1 16 0c0 5-4 7-4 11z"/><line x1="12" y1="25" x2="20" y2="25"/><line x1="13" y1="28" x2="19" y2="28"/><path d="M14 14l2 3 2-3"/><line x1="16" y1="0.5" x2="16" y2="1.5"/><line x1="4" y1="5" x2="5" y2="6"/><line x1="28" y1="5" x2="27" y2="6"/></svg>
    <div class="label">Electricity</div>
  </div>
  <div class="category" style="left:687px">
    <svg viewBox="0 0 32 32"><path d="M2 12h6l3-3h6l4 4h4a3 3 0 0 1 3 3v2h-5v-1h-7l-3 2H2z"/><line x1="14" y1="9" x2="14" y2="5"/><line x1="11" y1="5" x2="17" y2="5"/><circle cx="26" cy="26" r="1.8"/></svg>
    <div class="label">Water</div>
  </div>
  <div class="category" style="left:840px">
    <svg viewBox="0 0 32 32"><rect x="9" y="7" width="14" height="22" rx="3"/><rect x="12" y="3" width="8" height="4"/><line x1="9" y1="12" x2="23" y2="12"/><line x1="9" y1="24" x2="23" y2="24"/><path d="M16 14c-2 2-3 3-3 5a3 3 0 0 0 6 0c0-2-1-3-3-5z"/></svg>
    <div class="label">Natural Gas</div>
  </div>
  <div class="category" style="left:994px">
    <svg viewBox="0 0 32 32"><circle cx="5" cy="5" r="3.5"/><circle cx="16" cy="5" r="3.5"/><circle cx="27" cy="5" r="3.5"/><circle cx="5" cy="16" r="3.5"/><circle cx="16" cy="16" r="3.5"/><circle cx="27" cy="16" r="3.5"/><circle cx="5" cy="27" r="3.5"/><circle cx="16" cy="27" r="3.5"/><circle cx="27" cy="27" r="3.5"/></svg>
    <div class="label">Other</div>
  </div>

  <div class="search">
    <svg class="search-tag" viewBox="0 0 44 46"><path d="M2 0h32l10 23-10 23H2a2 2 0 0 1-2-2V2a2 2 0 0 1 2-2z" fill="#abd036"/><circle cx="20" cy="22" r="5.5" fill="none" stroke="#fff" stroke-width="2.4"/><line x1="24" y1="26" x2="27.5" y2="29.5" stroke="#fff" stroke-width="2.6" stroke-linecap="round"/></svg>
    <span class="search-text">Search for institutions</span>
  </div>
</section>

<h2 class="section-title">Select The Institution</h2>

<section class="institutions">
  <div class="vline" style="left:256px;top:0;height:323px"></div>
  <div class="vline" style="left:525px;top:161px;height:162px"></div>
  <div class="vline" style="left:795px;top:161px;height:162px"></div>
  <div class="hline" style="left:0;top:161px;width:1052px"></div>

  <div class="inst terra" style="left:0;top:0;width:256px;height:161px"><span class="mark"></span><span class="name">Terravolt</span></div>
  <div class="inst bright" style="left:257px;top:0;width:268px;height:161px"><span class="mark"></span><span class="name">Brightwell</span></div>
  <div class="inst terra focus" style="left:526px;top:0;width:269px;height:161px"><span class="mark"></span><span class="name">Terravolt</span></div>
  <div class="inst bright" style="left:796px;top:0;width:256px;height:161px"><span class="mark"></span><span class="name">Brightwell</span></div>

  <div class="inst bright" style="left:0;top:162px;width:256px;height:161px"><span class="mark"></span><span class="name">Brightwell</span></div>
  <div class="inst terra" style="left:257px;top:162px;width:268px;height:161px"><span class="mark"></span><span class="name">Terravolt</span></div>
  <div class="inst bright" style="left:526px;top:162px;width:269px;height:161px"><span class="mark"></span><span class="name">Brightwell</span></div>
  <div class="inst terra" style="left:796px;top:162px;width:256px;height:161px"><span class="mark"></span><span class="name">Terravolt</span></div>
</section>

<footer class="site-footer">
  <span class="item" style="left:74px">©2017 Company Name.</span>
  <span class="item" style="left:263px">Terms of Use</span>
  <span class="item" style="left:384px">Privacy</span>
  <span class="item" style="left:728px">Payment Method</span>
  <div class="card" style="left:872px;background:#e4e6e8;color:#1a2a6c">Cardex</div>
  <div class="card" style="left:937px;background:#2e6fb6;color:#fff">Paylon</div>
  <div class="card" style="left:1002px;background:#3b9ad9;color:#fff">Ambrix</div>
  <div class="card" style="left:1067px;background:#f37122;color:#fff">Vistro</div>
</footer>
</body>
</html>
```